Create a memorable Stationary for Security Software Company

TelVandrik is the worldwide leader in securing the Internet. Making Internet communications and critical data secure, reliable and available everywhere has been and continues to be our ongoing vision. We are committed to staying focused on real customer needs and to developing new and innovative security solutions that redefine the security landscape.

Industry/Entity Type

Internet

Font styles to use
Serif
Sans Serif
Script

Colors
0792cd
33a6d7
85cae6

```html
<!DOCTYPE html>
<html lang="en">
<head>
<meta charset="utf-8">
<title>TelVandrik Stationery</title>
<link href="https://fonts.googleapis.com/css2?family=Questrial&display=swap" rel="stylesheet">
<style>
:root{
  --blue-deep:#0792cd;
  --blue-main:#1ba1d9;
  --blue-mid:#33a6d7;
  --blue-soft:#85cae6;
  --paper:#ffffff;
  --sheet:#e9ebec;
  --stage:#ececec;
  --ink:#222;
}
*{box-sizing:border-box;margin:0;padding:0}
html,body{width:1200px;height:1043px;overflow:hidden}
body{background:var(--stage);font-family:"Questrial",sans-serif;position:relative}
.piece{position:absolute;overflow:hidden;box-shadow:0 2px 6px rgba(0,0,0,.15)}
.cloud-area{position:absolute}
.brand{display:flex;align-items:center;gap:.35em;color:var(--blue-deep);font-weight:400;white-space:nowrap}
.brand-dot{width:.8em;height:.8em;border-radius:50%;background:var(--blue-mid);flex:none}

/* folder cover */
.folder-cover{left:50px;top:40px;width:470px;height:660px;background:var(--blue-main)}
.folder-cover .cloud-area{left:22px;top:150px;width:426px;height:380px;background:var(--paper);border-radius:150px 120px 170px 140px}
.folder-cover .brand{position:absolute;left:0;right:0;top:305px;justify-content:center;font-size:40px}
.folder-cover .site{position:absolute;left:0;right:0;top:380px;text-align:center;color:var(--blue-deep);font-size:19px}

/* letterhead */
.letterhead{left:560px;top:40px;width:440px;height:620px;background:var(--sheet)}
.letterhead .cloud-area{left:0;top:0;width:440px;height:90px;background:linear-gradient(180deg,#f4fafd,var(--sheet))}
.letterhead .brand{position:absolute;left:40px;top:36px;font-size:20px}
.letter-body{position:absolute;left:44px;top:150px;width:350px;font-size:8px;line-height:1.35;color:var(--ink)}
.letter-body h2{font-size:10px;margin-bottom:20px;font-weight:400}
.letter-body p{margin-bottom:9px}

/* business cards */
.card{width:190px;height:106px;background:var(--paper)}
.card-front{left:58px;top:752px}
.card-front .brand{position:absolute;left:0;right:0;top:30px;justify-content:center;font-size:18px}
.card-front .site{position:absolute;left:0;right:0;top:70px;text-align:center;font-size:8px;color:var(--blue-deep)}
.card-back{left:58px;top:890px;background:var(--blue-main)}
.card-back .cloud-area{left:6px;top:26px;width:178px;height:76px;background:var(--paper);border-radius:30px}
.card-back .brand{position:absolute;left:0;right:0;top:6px;justify-content:center;font-size:14px;color:var(--paper)}
.card-back .brand .brand-dot{background:var(--paper)}
.card-back .details{position:absolute;left:0;right:0;top:42px;text-align:center;font-size:6.5px;line-height:1.45;color:var(--blue-deep)}
.card-back .details .name{font-size:7px;color:var(--ink)}

/* envelope front */
.envelope-front{left:290px;top:735px;width:400px;height:250px;background:var(--blue-main)}
.envelope-front .cloud-area{left:0;top:70px;width:200px;height:180px;background:var(--paper);border-radius:0 110px 0 0}
.envelope-front .brand{position:absolute;left:40px;top:150px;font-size:19px}
.envelope-front .return{position:absolute;left:40px;top:195px;font-size:7px;line-height:1.45;color:var(--blue-deep)}

/* envelope back */
.envelope-back{left:715px;top:700px;width:430px;height:300px;background:var(--blue-mid)}
.envelope-back .cloud-area{left:0;top:0;width:430px;height:95px;background:var(--paper);border-radius:0 0 24px 24px}
.envelope-back .flap-line{position:absolute;left:0;top:95px;width:430px;height:3px;background:var(--blue-deep)}
.envelope-back .sender{position:absolute;right:28px;top:250px;text-align:right;font-size:7px;line-height:1.5;color:var(--paper)}
</style>
</head>
<body>

<section class="piece folder-cover">
  <div class="cloud-area" role="img" aria-label="Soft white cloud illustration framed by blue clouds"></div>
  <div class="brand"><span class="brand-dot"></span>TelVandrik</div>
  <div class="site">telvandrik.com</div>
</section>

<section class="piece letterhead">
  <div class="cloud-area" role="img" aria-label="Row of outlined clouds along the top edge"></div>
  <div class="brand"><span class="brand-dot"></span>TelVandrik</div>
  <div class="letter-body">
    <h2>Lorem Ipsum</h2>
    <p>Lorem ipsum dolor sit amet, consectetur adipiscing elit. Proin non posuere nisl. Ut fringilla sapien nisi. Nunc ac feugiat erat. Proin vel arcu sed odio posuere hendrerit. Sed viverra purus erat, vitae volutpat nulla dapibus sed. Mauris a leo vitae lorem tempus iaculis ac in diam. Mauris venenatis vitae metus vitae volutpat. Aliquam erat volutpat. Praesent aliquam diam vel odio hendrerit, a efficitur dui sollicitudin. Nulla varius diam et pellentesque tincidunt. Sed faucibus eu massa quis venenatis. Suspendisse turpis libero, viverra sed aliquam quis, pulvinar non ligula. Integer viverra, nulla vitae egestas blandit, mauris ante commodo arcu, eu bibendum mauris tellus pulvinar orci. Proin ipsum nisi, consequat non finibus tristique, malesuada a velit.</p>
    <p>Proin rhoncus nunc vitae massa fermentum, in tempus nisi tempor. Donec nec efficitur augue. Mauris sagittis eleifend nulla sit amet sodales. Donec ultricies tempor nunc id convallis. Integer libero sem, varius nec nisl vitae, consectetur facilisis orci. Vestibulum non tortor varius, auctor nunc at, maximus metus. In non augue at nibh eleifend maximus. Sed suscipit congue ipsum, eu aliquet diam volutpat at. Integer sed venenatis augue, vel vulputate massa.</p>
    <p>Suspendisse potenti. Sed at sapien sit amet dolor luctus lacinia a ut ligula. Nulla nec magna condimentum, placerat neque a, vestibulum orci. Sed tristique quam quis sapien efficitur mollis. Morbi fringilla magna quam, ac hendrerit turpis dapibus non. Phasellus eu ornare dui. Sed id finibus massa. Lorem ipsum dolor sit amet, consectetur adipiscing elit.</p>
  </div>
</section>

<section class="piece card card-front">
  <div class="brand"><span class="brand-dot"></span>TelVandrik</div>
  <div class="site">telvandrik.com</div>
</section>

<section class="piece card card-back">
  <div class="cloud-area" role="img" aria-label="White cloud shape on blue"></div>
  <div class="brand"><span class="brand-dot"></span>TelVandrik</div>
  <div class="details">
    <div class="name">NAME OF SOMEBODY</div>
    <div>Director</div>
    <div>55 4821.0307 &nbsp;|&nbsp; 55 4822.0918</div>
    <div>418 Harlow Av &nbsp;|&nbsp; Denton Ridge, CO 80410</div>
  </div>
</section>

<section class="piece envelope-front">
  <div class="cloud-area" role="img" aria-label="White cloud area among blue clouds"></div>
  <div class="brand"><span class="brand-dot"></span>TelVandrik</div>
  <div class="return">418 Harlow Av<br>Denton Ridge, CO 80410<br>55 4821.0307 &nbsp;|&nbsp; 55 4822.0918</div>
</section>

<section class="piece envelope-back">
  <div class="cloud-area" role="img" aria-label="Outlined white clouds on the envelope flap"></div>
  <div class="flap-line"></div>
  <div class="sender">Name of Somebody<br>418 Harlow Av &nbsp;|&nbsp; Denton Ridge, CO 80410</div>
</section>

</body>
</html>
```